Australian Trucking Company Requires Professional Looking Stationary

We require a professional looking stationary design that incorporates our newly designed logo.

Our business, called "Marlow Haul Contracting", provides contracting work, transport and logistics to business in Western Australia particularly with links to the mining sector.

We are a small business looking to expand and our new logo and our new stationary will help develop our brand image in our market place.

Target Market(s)

Businesses and Corporation with links to the Mining Sector

Industry/Entity Type

Small Business

Requirements
Must have
• The letterhead must have the following details:
The new logo

Text saying: "Marlow Holdings Pty Ltd (ACN 352 018 927) ATF The Marlow Discretionary Trust T/AS"
"ABN 72 483 910 615"
Address "P.O Box 817 Wexbridge WA, 6999"
Phone: 08 9555 0182
Email: marlowhaul@inboxmail.example

The text on the letterhead should be editable as the details are likely to change in the near future. Provision should be made for a website address all though one isn't available at the moment.

The styling, layout and font text is entirely up to the designer.

```html
<!DOCTYPE html>
<html lang="en">
<head>
<meta charset="utf-8">
<title>Marlow Haul Contracting — Letterhead</title>
<link rel="stylesheet" href="https://fonts.googleapis.com/css2?family=Open+Sans:wght@400;600;700&display=swap">
<style>
  :root {
    --backdrop: #a0a0a0;
    --paper: #ffffff;
    --brand-dark: #8b0d10;
    --brand-bright: #ee1c24;
    --ink: #6b6b6b;
    --rule-grey: #9a9a9a;
    --watermark: #f1f1f1;
  }
  * { margin: 0; padding: 0; box-sizing: border-box; }
  html, body {
    width: 1069px;
    height: 1200px;
    overflow: hidden;
    background: var(--backdrop);
    font-family: "Open Sans", Arial, sans-serif;
  }
  .letterhead {
    position: absolute;
    left: 153px;
    top: 124px;
    width: 776px;
    height: 1003px;
    background: var(--paper);
    overflow: hidden;
  }
  .brand {
    position: absolute;
    left: 40px;
    top: 66px;
    display: flex;
    align-items: center;
    gap: 14px;
  }
  .brand-mark {
    width: 56px;
    height: 56px;
    background: var(--brand-dark);
  }
  .brand-name {
    font-weight: 700;
    font-size: 24px;
    line-height: 1.05;
    color: var(--brand-dark);
    text-transform: uppercase;
    letter-spacing: 0.5px;
  }
  .contact {
    position: absolute;
    left: 525px;
    top: 56px;
    font-size: 11.5px;
    line-height: 15.5px;
    color: var(--ink);
  }
  .contact .entity { color: var(--brand-dark); font-weight: 600; }
  .contact .label { color: var(--brand-dark); font-weight: 700; }
  .contact .address { margin-top: 9px; }
  .watermark {
    position: absolute;
    left: 260px;
    top: 520px;
    width: 516px;
    height: 438px;
    background: radial-gradient(ellipse at 65% 60%, #ececec 0%, var(--watermark) 45%, rgba(255,255,255,0) 80%);
  }
  .footer-rule {
    position: absolute;
    left: 28px;
    top: 962px;
    width: 720px;
    height: 12px;
  }
  .website {
    position: absolute;
    right: 29px;
    top: 978px;
    font-size: 12px;
    color: var(--brand-dark);
  }
</style>
</head>
<body>
  <main class="letterhead">
    <header class="brand">
      <span class="brand-mark"></span>
      <span class="brand-name">Marlow Haul<br>Contracting</span>
    </header>

    <address class="contact" style="font-style: normal;">
      <div><span class="entity">Marlow Holdings Pty Ltd</span>&nbsp; (ACN 352 018 927)</div>
      <div>ATF The Marlow Discretionary Trust T/AS</div>
      <div><span class="label">ABN</span> 72 483 910 615</div>
      <div class="address">P.O Box 817 Wexbridge WA, 6999</div>
      <div><span class="label">P.</span> 08 9555 0182</div>
      <div><span class="label">E.</span> marlowhaul@inboxmail.example</div>
    </address>

    <div class="watermark" role="img" aria-label="Faint large illustration of a prime-mover truck cab"></div>

    <svg class="footer-rule" viewBox="0 0 720 12" aria-hidden="true">
      <polygon points="0,0 596,0 591,7 0,7" fill="var(--brand-dark)"/>
      <polygon points="601,0 720,0 720,7 596,7" fill="var(--brand-bright)"/>
      <rect x="0" y="9" width="720" height="1" fill="var(--rule-grey)"/>
    </svg>

    <footer class="website">www.marlowhaul.example</footer>
  </main>
</body>
</html>
```